Powerpoint Deign for a sales presentation

I am looking for a powerpoint presentation design with animations of my Kindle Bright Lantern Method Blueprint
I would like this to be a path that leads from feeling sad to feeling awesome- due to finding your life purpose (your why)

There are 3 main areas that the client needs to know in order to find their why (purpose) Awareness - Intention & Manifest - these should be designed in grey (as this represents the grey miserable world they stay stuck in if they don't have these skills) and each word will need to be animated to come on one at a time

Each of these has 2 solutions that sits under the required steps
Awareness - The Beacon Sharpening Routine & The Lucid Insight Builder
Intention - The T.O.N.E Balance Tuner & The Glowing Tomorrow Glimpse
Manifest - The Lively Horizon Mandate & The Triumphant Spark Method

& a bonus system called The Kestrel Bloom Booster - which can be designed to be shown on a separate slide

These "solutions" should be in colour boxes that compliment our branding of red, white & black or even the orange as shown on the examples
I have a version now - but it has been put together over time & look like it doesn't sit together well, and we have added more along the way.
For example the path goes down rather than up (to success)
There is a sad face at the start & then a happy one - it would be better for the happy one to be at the end
The icons are all ok - but the trampoline one can go

Looking for new ideas and revamped ideas

Target Market(s)

40+ years old (mainly women but not always)

Industry/Entity Type

Personal Development

Other font styles liked:
• Merge

Colors
F0912C
F2A743
F7CA91
FBE8D2
FDF5EE
EB3D1F
EC4F4E
F09395
F8D3D4
FCEDEE

Requirements
Must have
• animation on the power point

```html
<!DOCTYPE html>
<html lang="en">
<head>
<meta charset="utf-8">
<title>Lantern Path – Journey Slides</title>
<link rel="stylesheet" href="https://fonts.googleapis.com/css2?family=Varela+Round&display=swap">
<style>
  :root {
    --sheet-bg: #4d5150;
    --slide-bg: #ffffff;
    --select-border: #ec6a4f;
    --ink: #111111;
    --label: #f2f2f2;
    --grey-pill: #d2d0d1;
    --grey-face: #bdbdbd;
    --grey-ring: #c9c9c9;
    --brand-red: #eb3d1f;
    --red-strong: #ec4f4e;
    --red-mid: #f09395;
    --red-soft: #f8d3d4;
    --sun: #f7c51e;
  }
  * { margin: 0; padding: 0; box-sizing: border-box; }
  html, body { width: 1200px; height: 728px; overflow: hidden; }
  body {
    background: var(--sheet-bg);
    font-family: "Varela Round", "Helvetica Neue", Arial, sans-serif;
    position: relative;
  }
  .slide {
    position: absolute;
    width: 560px;
    height: 313px;
    background: var(--slide-bg);
    border-radius: 3px;
  }
  .slide--grey { left: 11px; top: 10px; }
  .slide--colour { left: 607px; top: 10px; }
  .slide--notes {
    left: 10px; top: 376px; width: 562px; height: 317px;
    border: 3px solid var(--select-border);
    border-radius: 5px;
  }
  .slide svg { display: block; }
  .slide-number {
    position: absolute;
    color: var(--label);
    font-size: 13px;
  }
  .step-title { font-size: 16px; fill: var(--ink); }
  .step-subtitle { font-size: 7.2px; fill: var(--ink); }
  .brand-name { font-size: 9px; fill: var(--brand-red); }
  .journey-path {
    fill: none; stroke: var(--ink); stroke-width: 2.6;
    stroke-linecap: round; stroke-dasharray: 0 5.2;
  }
  .notes-text {
    position: absolute;
    left: 86px; top: 76px;
    width: 400px;
    font-size: 10.4px;
    line-height: 1.3;
    color: var(--ink);
  }
  .notes-text p { margin-bottom: 14px; }
</style>
</head>
<body>

<!-- Slide 1: grey world -->
<section class="slide slide--grey">
  <svg width="560" height="313" viewBox="0 0 560 313">
    <g class="brand">
      <circle cx="48" cy="38" r="6" fill="var(--brand-red)"/>
      <text class="brand-name" x="30" y="60">Lantern Path</text>
    </g>
    <path class="journey-path" d="M66 284 C100 272 125 258 138 239 C160 205 180 175 191 147 C200 120 206 90 210 59"/>

    <g class="step step--manifest">
      <rect x="223" y="36" width="300" height="45" rx="22.5" fill="var(--grey-pill)"/>
      <circle cx="242" cy="58" r="15" fill="#fff" role="img" aria-label="Signpost icon"/>
      <circle cx="242" cy="58" r="5" fill="var(--brand-red)"/>
      <circle cx="210" cy="59" r="7" fill="#fff" stroke="var(--grey-ring)" stroke-width="2.5"/>
      <circle cx="210" cy="59" r="2.2" fill="var(--grey-ring)"/>
      <circle cx="175" cy="60" r="16" fill="var(--grey-face)" role="img" aria-label="Laughing emoji"/>
      <text class="step-title" x="264" y="57">Manifest</text>
      <text class="step-subtitle" x="264" y="70">The Lively Horizon Mandate &amp; The Triumphant Spark Method</text>
    </g>

    <g class="step step--intention">
      <rect x="208" y="125" width="305" height="45" rx="22.5" fill="var(--grey-pill)"/>
      <circle cx="227" cy="147" r="15" fill="#fff" role="img" aria-label="Lightbulb icon"/>
      <circle cx="227" cy="147" r="5" fill="var(--red-mid)"/>
      <circle cx="191" cy="147" r="7" fill="#fff" stroke="var(--grey-ring)" stroke-width="2.5"/>
      <circle cx="191" cy="147" r="2.2" fill="var(--grey-ring)"/>
      <circle cx="156" cy="147" r="16" fill="var(--grey-face)" role="img" aria-label="Smiling emoji"/>
      <text class="step-title" x="252" y="148">Intention</text>
      <text class="step-subtitle" x="252" y="160">The T.O.N.E Balance Tuner &amp; The Glowing Tomorrow Glimpse</text>
    </g>

    <g class="step step--awareness">
      <rect x="154" y="220" width="332" height="44" rx="22" fill="var(--grey-pill)"/>
      <circle cx="173" cy="242" r="15" fill="#fff" role="img" aria-label="Compass icon"/>
      <circle cx="173" cy="242" r="5" fill="var(--brand-red)"/>
      <circle cx="138" cy="239" r="7" fill="#fff" stroke="var(--grey-ring)" stroke-width="2.5"/>
      <circle cx="138" cy="239" r="2.2" fill="var(--grey-ring)"/>
      <circle cx="107" cy="225" r="16" fill="var(--grey-face)" role="img" aria-label="Sad emoji"/>
      <text class="step-title" x="194" y="242">Awareness</text>
      <text class="step-subtitle" x="194" y="254">The Beacon Sharpening Routine &amp; The Lucid Insight Builder</text>
    </g>
  </svg>
</section>
<span class="slide-number" style="left:11px;top:338px;">1</span>

<!-- Slide 2: colour world -->
<section class="slide slide--colour">
  <svg width="560" height="313" viewBox="0 0 560 313">
    <defs>
      <linearGradient id="pill-manifest" x1="0" x2="1">
        <stop offset="0" stop-color="#ee4a49"/><stop offset="1" stop-color="var(--red-strong)"/>
      </linearGradient>
      <linearGradient id="pill-intention" x1="0" x2="1">
        <stop offset="0" stop-color="#ee8e90"/><stop offset="1" stop-color="var(--red-mid)"/>
      </linearGradient>
    </defs>
    <g class="brand">
      <circle cx="48" cy="38" r="6" fill="var(--brand-red)"/>
      <text class="brand-name" x="30" y="60">Lantern Path</text>
    </g>
    <path class="journey-path" d="M66 284 C100 272 125 258 138 239 C160 205 180 175 191 147 C200 120 206 90 210 59"/>

    <g class="step step--manifest">
      <rect x="223" y="36" width="300" height="45" rx="22.5" fill="url(#pill-manifest)"/>
      <circle cx="242" cy="58" r="15" fill="#fff" role="img" aria-label="Signpost icon"/>
      <circle cx="242" cy="58" r="5" fill="var(--brand-red)"/>
      <circle cx="210" cy="59" r="7" fill="#fff" stroke="var(--brand-red)" stroke-width="2.5"/>
      <circle cx="210" cy="59" r="2.2" fill="var(--brand-red)"/>
      <circle cx="175" cy="60" r="16" fill="var(--sun)" role="img" aria-label="Laughing emoji"/>
      <text class="step-title" x="264" y="57">Manifest</text>
      <text class="step-subtitle" x="264" y="70">The Lively Horizon Mandate &amp; The Triumphant Spark Method</text>
    </g>

    <g class="step step--intention">
      <rect x="208" y="125" width="305" height="45" rx="22.5" fill="url(#pill-intention)"/>
      <circle cx="227" cy="147" r="15" fill="#fff" role="img" aria-label="Lightbulb icon"/>
      <circle cx="227" cy="147" r="5" fill="var(--red-mid)"/>
      <circle cx="191" cy="147" r="7" fill="#fff" stroke="var(--red-mid)" stroke-width="2.5"/>
      <circle cx="191" cy="147" r="2.2" fill="var(--red-mid)"/>
      <circle cx="156" cy="147" r="16" fill="var(--sun)" role="img" aria-label="Smiling emoji"/>
      <text class="step-title" x="252" y="148">Intention</text>
      <text class="step-subtitle" x="252" y="160">The T.O.N.E Balance Tuner &amp; The Glowing Tomorrow Glimpse</text>
    </g>

    <g class="step step--awareness">
      <rect x="154" y="220" width="332" height="44" rx="22" fill="var(--red-soft)"/>
      <circle cx="173" cy="242" r="15" fill="#fff" role="img" aria-label="Compass icon"/>
      <circle cx="173" cy="242" r="5" fill="var(--brand-red)"/>
      <circle cx="138" cy="239" r="7" fill="#fff" stroke="var(--red-soft)" stroke-width="2.5"/>
      <circle cx="138" cy="239" r="2.2" fill="var(--red-soft)"/>
      <circle cx="107" cy="225" r="16" fill="var(--sun)" role="img" aria-label="Sad emoji"/>
      <text class="step-title" x="194" y="242">Awareness</text>
      <text class="step-subtitle" x="194" y="254">The Beacon Sharpening Routine &amp; The Lucid Insight Builder</text>
    </g>
  </svg>
</section>
<span class="slide-number" style="left:606px;top:338px;">2</span>

<!-- Slide 3: notes -->
<section class="slide slide--notes">
  <div class="notes-text">
    <p>For the client:</p>
    <p>1.&nbsp;&nbsp;&nbsp; I hope I understood correctly your design, otherwise let me know</p>
    <p>2. Can you give me more information about the "The Kestrel Bloom Booster"?</p>
    <p>3. Everything can be adjusted: colour, graphics, emojis... just let me know.</p>
    <p>Thanks</p>
  </div>
</section>
<span class="slide-number" style="left:11px;top:704px;">3</span>

</body>
</html>
```